Greek Souvlaki Restaurant Menu Design

We would like to redesign our menu (at the moment just a price-list without any graphics) and create something more fun.

You can find all the items we are offering at the following link / our e-shop:
https://fennelandfig.example/orders/en/order/
I have also attached a printout of the above with hand written notes on the sections and items that will be included.

Our menu is divided to a couple of parts:
- Souvlaki Bar and Grill
- Authentic Greek Cuisine
- Wine List
- Desserts
- Bakaliko

This project will take on the first part of our menu, which is the Souvlaki Bar and Grill. If we are happy with your design, we will then develop the rest of our menu.

Souvlaki Bar and Grill
---------------------------

Our souvlaki can be customised to the customer requirements. The following links have similar set ups:

WOWZA!Bun
https://pinboard.example/pin/100000000000000001/
I like the way they have set it up, but the graphics and colours used are not my thing. I also like they way they have split up the steps, choose, top it of, etc.

The Crisp
https://pinboard.example/pin/100000000000000002/
I hate the step 1,2,3 on the left side. It does not make it playful. Like the fact that they have used pictures of the ingredients.

https://pinboard.example/pin/100000000000000003/
Hate the graphics, like the concept.

-------------

First Sections: Our Souvliaki Pita Wrap

The steps to customise a souvlaki can be found on the following link:
https://fennelandfig.example/orders/en/order/ and choose pita wrap.

Most of the one side of our Souvliaki/Grill menu should be dedicated to our Pita Wraps.

It should have a small description of the Greek Souvlaki Pita Wrap. Something along the lines of "Get a whole meal all wrapped up with our delicious Greek Pita Wraps. Containing protein, sauce and salad". Improvements of this line are welcome.

It should then have the steps to customise it.

Step One.
Choose Base:
1. Chicken Skewer
2. Pork Skewer
3. etc
Price and options can be found on the above link on our website

Step Two.
Add one of our delicious home made sauces.
Options can be found on our website.

Step Three
Finalise it with the ingredients of your choice.
The customer can select multiple incredients

Step Four.
Feeling Hungry? Add extras:
Extras and Prices can be found on the link provided.

Buy two wraps and save. Takeaway only!
You will find this option as "Double Souvlaki Pita Wrap Offer."
Instead of 2x5.5 = £11 pay £10.5. This offer should also be mentioned somewhere on this section.

-----

Second Section - Our Platters

Skewers Platter and Gyros Platter

Options can be found by clicking on the items on the link provided.

Extras and Pita Bread option are common. Meat options are different and skewers have a choice of side. Meat options have 2/3 skewers and 200/300 grams of gyros, so they can probably be combined somehow.

These section can also be called Naked / Open Souvlaki Platters

Third Section
From Our Grill

All options from this section together with modifiers (can be see if you click on each item). I would like pictures from each item.

Forth Section
Meal Deals, starter combo and Set Menu.

Meal Deal for 1/2 and 4 are wraps with extras. The for 4 is not on the pdf and will be up on our website soon, so please check. I think those are easy to e incorporated next to the pita wrap section as upgrades to save.

Set menus are various items.

If they can fit on this page somehow we incorporate them, if not we can make a separate page with the offers / meals deals. If a separate page is created them the meal deal from our kitchen and vegetarean set menu should also be included.

Fifth Section
Salads and Starter

I would like all options from Hot and Cold starter and our salad. I would like pictures next to all options, if possible.

-----

Final notes/ideas.

Wraps, platters and grill could be one page front and back. Salads and starters could be a different page(s) or sections.

The menu should be easily updated and we would like a format where we can update prices and descriptions.

Prices and descriptions can be found on the link provided.

Feel free to improve our descriptions and titles. Please do mention where you made improvements, so we can approve them.

Our kitchen, dessert and wine menu will be given as a separate project and priority will be given to the person that won this competition.

If you need better quality pictures please let us know, most of the pictures we do have them in raw format too.

------

Some designs that I like. To give you an idea of the design I would like to see:

https://www.craftstall.example/listing/200000001/american-menu-restaurant-cafe-menus
I would love to see something like that for the grill/salad/starter side of our menu, since it has space for pictures.

https://pinboard.example/pin/100000000000000004/
I would love to see something like that, where the incredients of a souvlaki come together. This is optional and does not have to be there.

https://pinboard.example/pin/100000000000000005/

https://pinboard.example/pin/100000000000000006/

https://pinboard.example/pin/100000000000000007/

https://pinboard.example/pin/100000000000000008/

Target Market(s)

London

Font styles to use
Serif
Sans Serif

Colors
abd037
3277b5
33a6d7

Requirements
Must have
• Build your own souvlaki section. See description for examples.

Pictures for starters and salads.

Should be elegant
Nice to have
• Incorporate our relevant meal deals on the souvlaki pita section

```html
<!DOCTYPE html>
<html lang="en">
<head>
<meta charset="utf-8">
<title>Fennel &amp; Fig — Souvlaki Platters</title>
<link href="https://fonts.googleapis.com/css2?family=Lato:wght@300;400;700;900&family=Lobster&display=swap" rel="stylesheet">
<style>
  :root{
    --ink:#1d1d1d;
    --paper:#ffffff;
    --backdrop:#dcdce0;
    --muted:#8a8a8a;
    --rule:#9a9a9a;
    --meat:#6b3a1e;
    --meat-light:#a8683a;
    --bread:#f2c393;
    --fries:#f0b72a;
    --tomato:#e0412b;
    --salad:#5f8f3e;
    --sauce:#d7e8d7;
    --cheese:#efc27a;
  }
  *{box-sizing:border-box;margin:0;padding:0}
  html,body{width:1200px;height:1200px;overflow:hidden;background:var(--backdrop)}
  body{font-family:'Lato',sans-serif;color:var(--ink);position:relative}
  .sheet{position:absolute;left:185px;top:14px;width:830px;height:1172px;background:var(--paper)}
  .abs{position:absolute}

  .brand{left:52px;top:26px;width:112px;text-align:center;font-weight:700;font-size:22px;line-height:1.05;letter-spacing:1px;text-transform:uppercase;color:var(--ink)}
  .brand .dot{display:inline-block;width:10px;height:10px;border-radius:50%;background:var(--ink);margin-top:8px}

  .title-band{left:183px;top:47px;width:616px;height:59px}
  .title-band svg{position:absolute;inset:0}
  .title-band h1{position:relative;font-family:'Lobster',sans-serif;font-weight:400;color:var(--paper);font-size:40px;text-align:center;line-height:59px;letter-spacing:1px}

  .frame{left:31px;top:129px;width:769px;height:1013px;border:3px solid var(--ink)}
  .divider{left:31px;top:629px;width:769px;height:3px;background:var(--ink)}

  .dish-title{font-weight:700;font-size:28px;letter-spacing:-.3px;white-space:nowrap}
  .dish-title .price{font-weight:400;font-size:19px;color:var(--muted);letter-spacing:0}
  .dish-desc{font-weight:300;font-size:14px;line-height:18px;width:730px}

  .photo{border-radius:50%}
  .photo-gyros{left:53px;top:282px;width:258px;height:190px;background:radial-gradient(ellipse at 45% 40%,#7a4a28 0%,#b98a4a 35%,#e2553a 62%,#f4f1ec 75%,#e8e4de 100%)}
  .photo-skewers{left:58px;top:786px;width:336px;height:108px;border-radius:14px;background:linear-gradient(90deg,#f0c04a 0%,#c08040 40%,#a8683a 60%,#d9a050 85%,#eee9df 100%)}

  .group-head{border-top:1px solid var(--rule);border-bottom:1px solid var(--rule);text-align:center;font-weight:700;font-size:16px;letter-spacing:2px;text-transform:uppercase;height:25px;line-height:24px}
  .col-head{font-style:italic;font-size:14px;position:absolute}
  .row{position:absolute;display:flex;align-items:center;font-size:15px;white-space:nowrap}
  .row .name{font-weight:400;line-height:16px}
  .row .add{position:absolute;color:var(--muted);font-size:14px;text-align:center}
  .thumb{position:absolute;border-radius:50%}
  .thumb-meat{width:50px;height:34px;border-radius:40% 55% 45% 50%;background:radial-gradient(circle at 40% 40%,var(--meat-light),var(--meat) 70%)}
  .thumb-skewer{width:60px;height:22px;border-radius:10px;background:linear-gradient(90deg,var(--meat),var(--meat-light),var(--meat))}
  .thumb-pita{width:44px;height:44px;background:radial-gradient(circle at 45% 40%,#f8d6b0,var(--bread))}
  .thumb-pita2{width:62px;height:50px;border-radius:48%;background:radial-gradient(circle at 60% 45%,#f8d6b0,var(--bread) 70%)}
  .thumb-cheese{width:44px;height:32px;border-radius:8px;background:linear-gradient(135deg,var(--cheese),#fff3dc 50%,var(--cheese))}
  .thumb-sauce{width:40px;height:40px;background:radial-gradient(circle,#fff,var(--sauce) 60%,#c9d6c9)}
  .thumb-fries{width:52px;height:30px;border-radius:6px;background:linear-gradient(120deg,var(--fries),#ffd65c,var(--fries))}
  .thumb-salad{width:40px;height:40px;background:radial-gradient(circle,var(--tomato) 0%,var(--salad) 45%,#3d5c28 100%)}
  .dots{position:absolute;width:42px;border-top:2px dotted #9a9a9a}
</style>
</head>
<body>
<div class="sheet">
  <div class="abs brand">Fennel<br>&amp; Fig<br><span class="dot"></span></div>

  <div class="abs title-band">
    <svg width="616" height="59" viewBox="0 0 616 59"><polygon points="0,0 616,0 586,29.5 616,59 0,59 30,29.5" fill="#1d1d1d"/></svg>
    <h1>Souvlaki</h1>
  </div>

  <div class="abs frame"></div>
  <div class="abs divider"></div>

  <!-- Gyros platter -->
  <section class="gyros-platter">
    <h2 class="abs dish-title" style="left:53px;top:145px">GYROS PLATTER <span class="price">£ 13.00</span></h2>
    <p class="abs dish-desc" style="left:53px;top:187px">Traditional Greek Juicy Pork or Chicken Gyros. Generous portion served with refreshing tzatziki sauce, pita bread, fries, onion, tomatoes and lettuce. A great selection of ingredients make it a delicious complete meal!</p>
    <div class="abs photo photo-gyros" role="img" aria-label="Gyros platter with fries, sliced meat, tomatoes, onion and tzatziki"></div>

    <div class="abs" style="left:332px;top:246px;width:438px">
      <div class="group-head">Meat options</div>
    </div>
    <span class="col-head" style="left:587px;top:277px">200grams</span>
    <span class="col-head" style="left:690px;top:277px">300grams</span>

    <div class="thumb thumb-meat" style="left:352px;top:292px" role="img" aria-label="Chicken gyros"></div>
    <div class="row" style="left:446px;top:301px"><span class="name">Chicken Gyros</span></div>
    <span class="row" style="left:618px;top:301px;color:var(--muted)">-</span>
    <span class="row" style="left:696px;top:301px;color:var(--muted);font-size:14px">+ £ 3.50</span>

    <div class="thumb thumb-meat" style="left:358px;top:334px" role="img" aria-label="Pork gyros"></div>
    <div class="row" style="left:449px;top:343px"><span class="name">Pork Gryos</span></div>
    <span class="row" style="left:618px;top:343px;color:var(--muted)">-</span>
    <span class="row" style="left:696px;top:343px;color:var(--muted);font-size:14px">+ £ 3.50</span>

    <div class="thumb thumb-meat" style="left:348px;top:382px" role="img" aria-label="Mixed chicken and pork gyros"></div>
    <div class="row" style="left:446px;top:385px"><span class="name">Mixed Gryos<br>(chicken and pork)</span></div>
    <span class="row" style="left:592px;top:385px;color:var(--muted);font-size:14px">+ £ 1.00</span>
    <span class="row" style="left:696px;top:385px;color:var(--muted);font-size:14px">+ £ 4.50</span>

    <div class="abs" style="left:332px;top:451px;width:185px"><div class="group-head">Pita bread</div></div>
    <span class="dots" style="left:349px;top:492px"></span>
    <div class="row" style="left:408px;top:485px">No Pita</div>
    <div class="thumb thumb-pita" style="left:346px;top:512px" role="img" aria-label="One pita"></div>
    <div class="row" style="left:408px;top:527px">1 Pita</div>
    <div class="thumb thumb-pita2" style="left:337px;top:553px" role="img" aria-label="Two pitas"></div>
    <div class="row" style="left:408px;top:569px">2 Pita <span style="color:var(--muted);font-size:14px;margin-left:12px">+ £ 1.00</span></div>

    <div class="abs" style="left:538px;top:451px;width:232px"><div class="group-head">Extras</div></div>
    <div class="thumb thumb-cheese" style="left:552px;top:480px" role="img" aria-label="Haloumi"></div>
    <div class="row" style="left:610px;top:485px">Extra Haloumi<span style="color:var(--muted);font-size:14px;margin-left:3px">+ £ 3.50</span></div>
    <div class="thumb thumb-sauce" style="left:556px;top:518px" role="img" aria-label="Tzatziki"></div>
    <div class="row" style="left:610px;top:527px">Extra Tzatziki<span style="color:var(--muted);font-size:14px;margin-left:11px">+ £ 3.00</span></div>
  </section>

  <!-- Skewers platter -->
  <section class="skewers-platter">
    <h2 class="abs dish-title" style="left:53px;top:645px">SKEWERS PLATTER <span class="price">£ 10.00</span></h2>
    <p class="abs dish-desc" style="left:53px;top:687px;width:740px">Our delicious skewers or kebab. Homemade souvlaki is taken from the best part of the meat to create the perfect succulent grilled experience. Served with fries or salad and pitta bread.</p>
    <div class="abs photo photo-skewers" role="img" aria-label="Grilled skewers on a platter with fries and lemon"></div>

    <div class="abs" style="left:406px;top:755px;width:356px"><div class="group-head">Meat options</div></div>
    <span class="col-head" style="left:657px;top:786px">2x</span>
    <span class="col-head" style="left:732px;top:786px">3x</span>

    <div class="thumb thumb-skewer" style="left:426px;top:811px;transform:rotate(-25deg)" role="img" aria-label="Chicken skewer"></div>
    <div class="row" style="left:509px;top:810px">Chicken Skewers</div>
    <span class="row" style="left:659px;top:810px;color:var(--muted)">-</span>
    <span class="row" style="left:709px;top:810px;color:var(--muted);font-size:14px">+ £ 3.00</span>

    <div class="thumb thumb-skewer" style="left:420px;top:856px;transform:rotate(-25deg);background:linear-gradient(90deg,#c89a70,#e6c29a,#c89a70)" role="img" aria-label="Pork skewer"></div>
    <div class="row" style="left:512px;top:851px">Pork Skewers</div>
    <span class="row" style="left:659px;top:851px;color:var(--muted)">-</span>
    <span class="row" style="left:709px;top:851px;color:var(--muted);font-size:14px">+ £ 3.00</span>

    <div class="thumb thumb-skewer" style="left:432px;top:904px;width:48px;height:26px;transform:rotate(-30deg);background:linear-gradient(90deg,#3e2315,#6b3a1e,#3e2315)" role="img" aria-label="Lamb and beef kebab"></div>
    <div class="row" style="left:509px;top:893px"><span class="name">Kebab<br>(lamb+beef)</span></div>
    <span class="row" style="left:659px;top:893px;color:var(--muted)">-</span>
    <span class="row" style="left:709px;top:893px;color:var(--muted);font-size:14px">+ £ 3.00</span>

    <div class="abs" style="left:59px;top:965px;width:232px"><div class="group-head">Choose side</div></div>
    <div class="thumb thumb-fries" style="left:64px;top:995px" role="img" aria-label="Fries"></div>
    <div class="row" style="left:130px;top:999px">Fries</div>
    <div class="thumb thumb-salad" style="left:72px;top:1031px" role="img" aria-label="Side salad"></div>
    <div class="row" style="left:130px;top:1041px">Side Salad<span style="color:var(--muted);font-size:14px;margin-left:28px">+ £ 2.50</span></div>

    <div class="abs" style="left:321px;top:965px;width:185px"><div class="group-head">Pita bread</div></div>
    <span class="dots" style="left:338px;top:1006px"></span>
    <div class="row" style="left:397px;top:999px">No Pita</div>
    <div class="thumb thumb-pita" style="left:334px;top:1020px" role="img" aria-label="One pita"></div>
    <div class="row" style="left:397px;top:1041px">1 Pita</div>
    <div class="thumb thumb-pita2" style="left:326px;top:1068px" role="img" aria-label="Two pitas"></div>
    <div class="row" style="left:397px;top:1083px">2 Pita <span style="color:var(--muted);font-size:14px;margin-left:12px">+ £ 1.00</span></div>

    <div class="abs" style="left:538px;top:965px;width:232px"><div class="group-head">Extras</div></div>
    <div class="thumb thumb-cheese" style="left:552px;top:994px" role="img" aria-label="Haloumi"></div>
    <div class="row" style="left:610px;top:999px">Extra Haloumi<span style="color:var(--muted);font-size:14px;margin-left:3px">+ £ 3.50</span></div>
    <div class="thumb thumb-sauce" style="left:556px;top:1032px" role="img" aria-label="Tzatziki"></div>
    <div class="row" style="left:610px;top:1041px">Extra Tzatziki<span style="color:var(--muted);font-size:14px;margin-left:11px">+ £ 3.00</span></div>
  </section>
</div>
</body>
</html>
```